Gutschein-Design für Nähmaschinen Fachhandel
Zielgruppe
Wir sind ein Nähmaschinen Fachhandel und suchen einen Gutschein für beispielsweise 10% Nachlass auf unseren Online-Shop. Zielgruppe sind (Hobby-)Näherinnen jeden Alters.
Aufgabenstellung
Das Design sollte auf unseren Internetauftritt ( www.Stoffwerk-Kontor.de ) und Farben des Firmenlogos angelehnt sein. Das Design sollte Modern und im Nähstyle sein.
Folgendes soll die Frontseite des Flyers beinhalten:
- Unser Logo
- Nur einlösbar unter www.Stoffwerk-Kontor.de
- 10% AUF DEN NÄCHSTEN EINKAUF
- Gültig bis .............
- Code: ..............
Rückseite soll folgendes beinhalten:
- Werkzeug als Grafik ( hier sind wir offen )
- NÄHMASCHINEN MEISTERWERKSTATT
- Wir reparieren Nähmaschinen, Stickmaschinen, Overlock oder auch Coverlock aller Marken.
- Melden Sie sich gerne per WhatsApp, telefonisch oder per E-Mail.
Größe des Flyers:
- Länge 21cm
- Breite: 9,7 cm

```html
<!DOCTYPE html>
<html lang="de">
<head>
<meta charset="utf-8">
<title>Stoffwerk Kontor – Gutschein</title>
<link href="https://fonts.googleapis.com/css2?family=Gochi+Hand&family=Open+Sans:wght@400;600;700;800&display=swap" rel="stylesheet">
<style>
  :root{
    --red:#d0202a;
    --dark:#3c3c3c;
    --panel:#e3e3e3;
    --ink:#1d1d1d;
    --white:#ffffff;
    --paper:#f3f3f3;
  }
  html,body{margin:0;padding:0;width:849px;height:1200px;overflow:hidden;background:var(--white);}
  .sheet{position:absolute;left:0;top:0;width:1000px;height:1414px;transform:scale(.849);transform-origin:0 0;font-family:"Open Sans",Arial,sans-serif;color:var(--ink);}
  .card{position:absolute;left:179px;width:643px;height:298px;overflow:hidden;box-shadow:2px 3px 6px rgba(0,0,0,.35);background:var(--white);}
  .card--one{top:42px}.card--two{top:387px}.card--three{top:730px}.card--back{top:1075px;background:var(--paper)}
  .layer{position:absolute;left:0;top:0;width:643px;height:298px}
  .photo{position:absolute;top:0;right:0;height:298px}
  .photo--studio{left:268px;background:
      radial-gradient(ellipse 120px 150px at 62% 35%,#c9a98f 0%,rgba(201,169,143,0) 70%),
      radial-gradient(ellipse 140px 120px at 15% 75%,#6d8fb8 0%,rgba(109,143,184,0) 75%),
      linear-gradient(135deg,#ededed 0%,#e0e2e4 55%,#b8c4d2 100%)}
  .photo--flatlay{left:268px;background:
      radial-gradient(ellipse 150px 90px at 55% 22%,#3a3434 0%,rgba(58,52,52,0) 75%),
      radial-gradient(ellipse 80px 70px at 25% 78%,#f4f6f7 0%,rgba(244,246,247,0) 75%),
      linear-gradient(160deg,#7fc2d8 0%,#9fd2e3 50%,#c9e7f0 100%)}
  .photo--cart{left:0;background:
      radial-gradient(ellipse 80px 90px at 42% 58%,#9aa4aa 0%,rgba(154,164,170,0) 75%),
      radial-gradient(ellipse 60px 40px at 55% 33%,#f0c640 0%,rgba(240,198,64,0) 75%),
      linear-gradient(120deg,#cbe6f0 0%,#b9dcea 60%,#c6e3ee 100%)}
  .brand{position:absolute;left:30px;top:22px;display:flex;align-items:center;gap:12px;}
  .brand__name{font-weight:800;font-size:22px;line-height:22px;letter-spacing:.5px;color:var(--ink);text-transform:uppercase}
  .brand__mark{width:22px;height:22px;background:var(--red)}
  .offer{position:absolute;left:8px;width:240px;top:128px;text-align:center;font-family:"Gochi Hand",cursive;color:var(--white)}
  .offer__value{font-size:76px;line-height:72px;}
  .offer__text{font-size:30px;line-height:27px;margin-top:2px}
  .card--three .offer{color:var(--ink)}
  .card--three .offer__value{color:var(--red)}
  .code{position:absolute;left:432px;color:var(--white);font-weight:700}
  .code__label{top:161px;font-size:14px}
  .code__value{position:absolute;left:432px;top:188px;font-size:34px;font-weight:700;color:var(--ink);letter-spacing:.5px}
  .code__note{top:241px;font-size:13.5px;line-height:17px}
  .validity{position:absolute;left:631px;top:140px;transform:translate(-50%,-50%) rotate(-90deg);font-size:8px;white-space:nowrap;color:var(--ink)}
  .workshop__title{position:absolute;left:321px;top:22px;font-family:"Gochi Hand",cursive;font-size:29px;line-height:25px;text-transform:uppercase}
  .workshop__text{position:absolute;left:321px;top:82px;font-size:17px;line-height:23px;width:300px}
  .contact{position:absolute;left:30px;top:133px;font-size:14.5px;line-height:18px}
  .contact__row{display:flex;font-weight:700;font-size:14px}
  .contact__row span:first-child{width:78px}
  .contact__mail{color:var(--red);font-weight:700;font-size:14.5px}
  .footer{position:absolute;left:0;bottom:0;width:643px;height:47px;background:var(--dark);color:var(--white);font-size:12px;display:flex;align-items:center;padding-left:30px;box-sizing:border-box;gap:8px}
  .footer strong{font-weight:700}
  .footer__web{margin-left:10px;font-weight:700;font-size:14.5px}
</style>
</head>
<body>
<div class="sheet">

  <section class="card card--one">
    <div class="photo photo--studio" role="img" aria-label="Foto: lächelnde Näherin mit Schere an der Nähmaschine"></div>
    <svg class="layer" viewBox="0 0 643 298">
      <rect x="0" y="0" width="268" height="298" fill="var(--dark)"/>
      <polygon points="0,0 268,0 268,78 0,128" fill="var(--panel)"/>
      <polyline points="0,120 261,71 261,0" fill="none" stroke="var(--red)" stroke-width="1.3" stroke-dasharray="4 3"/>
      <rect x="268" y="0" width="3" height="80" fill="var(--red)"/>
      <polygon points="411,148 621,103 621,298 381,298" fill="var(--red)"/>
      <polyline points="391,298 421,158 610,116 610,298" fill="none" stroke="var(--white)" stroke-width="1.3" stroke-dasharray="4 3"/>
      <rect x="403" y="186" width="191" height="50" fill="var(--white)"/>
      <circle cx="271" cy="178" r="52" fill="var(--red)"/>
      <circle cx="271" cy="178" r="43" fill="none" stroke="var(--white)" stroke-width="1.3" stroke-dasharray="4 3"/>
      <text x="271" y="198" text-anchor="middle" font-family="Open Sans, sans-serif" font-weight="800" font-size="56" fill="var(--white)">%</text>
    </svg>
    <div class="brand"><span class="brand__name">Stoffwerk<br>Kontor</span><span class="brand__mark"></span></div>
    <div class="offer"><div class="offer__value">10%</div><div class="offer__text">AUF IHREN<br>NÄCHSTEN<br>EINKAUF</div></div>
    <div class="code code__label">Ihr persönlicher Code:</div>
    <div class="code__value">0XD128U</div>
    <div class="code code__note">Gutschein nur einlösbar<br>in unserem Online-Shop</div>
    <div class="validity">Gültig bis: xx.xx.xxxx</div>
  </section>

  <section class="card card--two">
    <div class="photo photo--flatlay" role="img" aria-label="Foto: Frau liegend zwischen Maßband, Stoffen und Nähmaschine auf hellblauem Grund"></div>
    <svg class="layer" viewBox="0 0 643 298">
      <rect x="0" y="0" width="268" height="298" fill="var(--dark)"/>
      <polygon points="0,0 268,0 268,78 0,128" fill="var(--panel)"/>
      <polyline points="0,120 261,71 261,0" fill="none" stroke="var(--red)" stroke-width="1.3" stroke-dasharray="4 3"/>
      <rect x="268" y="0" width="3" height="80" fill="var(--red)"/>
      <polygon points="411,148 621,103 621,298 381,298" fill="var(--red)"/>
      <polyline points="391,298 421,158 610,116 610,298" fill="none" stroke="var(--white)" stroke-width="1.3" stroke-dasharray="4 3"/>
      <rect x="403" y="186" width="191" height="50" fill="var(--white)"/>
      <circle cx="271" cy="178" r="52" fill="var(--red)"/>
      <circle cx="271" cy="178" r="43" fill="none" stroke="var(--white)" stroke-width="1.3" stroke-dasharray="4 3"/>
      <text x="271" y="198" text-anchor="middle" font-family="Open Sans, sans-serif" font-weight="800" font-size="56" fill="var(--white)">%</text>
    </svg>
    <div class="brand"><span class="brand__name">Stoffwerk<br>Kontor</span><span class="brand__mark"></span></div>
    <div class="offer"><div class="offer__value">10%</div><div class="offer__text">AUF IHREN<br>NÄCHSTEN<br>EINKAUF</div></div>
    <div class="code code__label">Ihr persönlicher Code:</div>
    <div class="code__value">0XD128U</div>
    <div class="code code__note">Gutschein nur einlösbar<br>in unserem Online-Shop</div>
    <div class="validity">Gültig bis: xx.xx.xxxx</div>
  </section>

  <section class="card card--three">
    <div class="photo photo--cart" role="img" aria-label="Foto: Einkaufswagen mit Garnrollen, Nadeln und Fingerhut auf hellblauem Grund, dahinter ein genähtes Prozentzeichen"></div>
    <svg class="layer" viewBox="0 0 643 298">
      <polygon points="0,0 268,0 268,78 0,128" fill="var(--panel)"/>
      <polyline points="0,120 261,71 261,0" fill="none" stroke="var(--red)" stroke-width="1.3" stroke-dasharray="4 3"/>
      <polygon points="411,148 621,103 621,298 381,298" fill="var(--red)"/>
      <polyline points="391,298 421,158 610,116 610,298" fill="none" stroke="var(--white)" stroke-width="1.3" stroke-dasharray="4 3"/>
      <rect x="403" y="186" width="191" height="50" fill="var(--white)"/>
    </svg>
    <div class="brand"><span class="brand__name">Stoffwerk<br>Kontor</span><span class="brand__mark"></span></div>
    <div class="offer"><div class="offer__value">10%</div><div class="offer__text">AUF IHREN<br>NÄCHSTEN<br>EINKAUF</div></div>
    <div class="code code__label">Ihr persönlicher Code:</div>
    <div class="code__value">0XD128U</div>
    <div class="code code__note">Gutschein nur einlösbar<br>in unserem Online-Shop</div>
    <div class="validity">Gültig bis: xx.xx.xxxx</div>
  </section>

  <section class="card card--back">
    <svg class="layer" viewBox="0 0 643 298">
      <rect x="0" y="128" width="265" height="122" fill="var(--white)"/>
      <rect x="300" y="68" width="320" height="182" fill="var(--white)"/>
      <polygon points="0,0 268,0 268,78 0,128" fill="var(--panel)"/>
      <polyline points="0,120 261,71 261,0" fill="none" stroke="var(--red)" stroke-width="1.3" stroke-dasharray="4 3"/>
      <g fill="var(--red)">
        <circle cx="353" cy="198" r="32"/><circle cx="429" cy="198" r="32"/>
        <circle cx="505" cy="198" r="32"/><circle cx="581" cy="198" r="32"/>
      </g>
      <g fill="none" stroke="var(--white)" stroke-width="1.2" stroke-dasharray="3.5 2.5">
        <circle cx="353" cy="198" r="26"/><circle cx="429" cy="198" r="26"/>
        <circle cx="505" cy="198" r="26"/><circle cx="581" cy="198" r="26"/>
      </g>
      <g fill="none" stroke="var(--white)" stroke-width="1.8" stroke-linejoin="round" stroke-linecap="round">
        <path d="M340 210 h28 M342 210 v-18 h24 v6 h-14 v12"/>
        <circle cx="360" cy="195" r="1.5"/>
        <path d="M418 208 l18 -18 a5 5 0 0 1 7 7 l-18 18 a5 5 0 0 1 -7 -7 z M424 203 l7 7"/>
        <path d="M500 184 h10 l-2 8 l8 22 h-22 l8 -22 z"/>
        <circle cx="578" cy="188" r="5"/>
        <path d="M570 214 v-10 a8 8 0 0 1 16 0 v10 M588 196 l6 16"/>
      </g>
    </svg>
    <div class="brand"><span class="brand__name">Stoffwerk<br>Kontor</span><span class="brand__mark"></span></div>
    <div class="contact">
      <div>Melden Sie sich per WhatsApp,<br>telefonisch oder per E-Mail:</div>
      <div style="height:9px"></div>
      <div class="contact__row"><span>Mobil</span><span>0151 2038846</span></div>
      <div class="contact__row"><span>Telefon</span><span>08761 - 4093</span></div>
      <div class="contact__mail">info@stoffwerk-kontor.de</div>
    </div>
    <div class="workshop__title">Nähmaschinen<br>Meisterwerkstatt</div>
    <div class="workshop__text">Wir reparieren Nähmaschinen, Stickmaschinen, Overlock oder auch Coverlock aller Marken.</div>
    <div class="footer"><strong>Stoffwerk Kontor</strong><span>Mühlenweg 17</span><span>84030 Ergolding</span><span class="footer__web">www.stoffwerk-kontor.de</span></div>
  </section>

</div>
</body>
</html>
```